Book cover for book entitled "Planting Gardens After Winter ....Plus Growing Bright Mornings Within"

I need a book cover for ebook and 6" x 9" paperback print book (print forge pod). I want a simple but "positive" cover with no gothic or darkness in design. I would prefer a "hopeful color scheme" in yellow, blue, green analogous colors and very easy to read main title "Planting Gardens After Winter". I want the tag line of the title. "plus grow bright mornings within" included on the cover please. I am not opposed to white in the color scheme I believe the graphic needs to somehow deal with doors, blocks, keys (perhaps a combination lock since the book is my story of healing from pancreatic cancer through faith, nutrition, and lifestyle changes). I am basically looking for the front cover from you but in a high definition format so it can be transferred to posters and banners for seminar displays. I am uploading my photo in case a designer would want to include a small copy of it in a design although I plan the photo to be on the back cover. The photo could, of course, be cropped.

I would also be interested in seeing a design with a woman  with arms folded and looking satisfied or victorious (happy) casually leaning against a closed door.    It can be very simple....

This graphic could be photo or drawing-even a good line drawing.   Almost whimsical would be okay.  This cover need not be highly complicated but I do want the title easy to read in small or large sizes for ebook and print book.

Reason: I have just changed to "committed" and some new "acceptances" have just come in.

Industry/Entity Type

Nutrition

Font styles to use
Serif

Colors
fbee3e
acd037
33b7a4
34a6d8
3377b5

```html
<!DOCTYPE html>
<html lang="en">
<head>
<meta charset="utf-8">
<title>Planting Gardens After Winter — Book Cover</title>
<link href="https://fonts.googleapis.com/css2?family=Cinzel:wght@400;600;700&display=swap" rel="stylesheet">
<style>
  :root {
    --sun: #f7e93c;
    --sun-pale: #f3ef8e;
    --sky-pale: #d6f1f1;
    --aqua: #8fd6e2;
    --teal: #33b7a4;
    --sea: #2faeb5;
    --blue: #34a6d8;
    --navy: #3377b5;
    --lime: #cfe24a;
    --white: #ffffff;
  }
  * { margin: 0; padding: 0; box-sizing: border-box; }
  html, body { width: 1021px; height: 1200px; overflow: hidden; }
  body { font-family: "Cinzel", "Times New Roman", serif; }

  .cover {
    position: relative;
    width: 1021px;
    height: 1200px;
    overflow: hidden;
    background: linear-gradient(180deg,
      var(--sun) 0%, var(--sun-pale) 17%, var(--sky-pale) 33%,
      #bfe9ee 50%, var(--aqua) 70%, #5cc6c9 88%, var(--sea) 100%);
  }

  .scene-doors {
    position: absolute;
    left: 395px; top: 405px;
    width: 626px; height: 795px;
    background:
      linear-gradient(90deg, rgba(120,180,190,0.25) 0%, rgba(240,250,250,0.55) 30%, rgba(225,245,246,0.6) 60%, rgba(120,190,200,0.3) 100%),
      linear-gradient(180deg, #c9ecef 0%, #a9dde5 55%, #5fc4c6 100%);
    opacity: 0.85;
  }

  .spine {
    position: absolute;
    left: 0; top: 0;
    width: 66px; height: 1200px;
  }
  .spine-title {
    position: absolute;
    left: 66px; top: 22px;
    transform-origin: 0 0;
    transform: rotate(90deg);
    white-space: nowrap;
    font-size: 54px;
    line-height: 1;
    font-weight: 600;
    color: var(--white);
    letter-spacing: 1px;
    -webkit-text-stroke: 1.5px var(--navy);
    paint-order: stroke fill;
  }
  .spine-title small { font-size: 36px; }

  .title { position: absolute; left: 0; top: 0; }
  .title-line {
    position: absolute;
    white-space: nowrap;
    line-height: 1;
    color: var(--navy);
    font-weight: 600;
    text-shadow:
      0 0 2px #fff, 2px 2px 0 #fff, -2px -2px 0 #fff, 2px -2px 0 #fff, -2px 2px 0 #fff,
      3px 0 0 #fff, -3px 0 0 #fff, 0 3px 0 #fff, 0 -3px 0 #fff,
      0 0 14px rgba(255,255,255,0.9);
  }
  .title-line .minor { font-size: 0.42em; vertical-align: 0.9em; margin-left: 10px; }
  .line-planting { left: 160px; top: 154px; font-size: 104px; }
  .line-gardens { left: 190px; top: 247px; font-size: 124px; }
  .line-winter { left: 220px; top: 348px; font-size: 160px; }

  .tagline {
    position: absolute;
    left: 0; top: 0;
    font-weight: 700;
    color: var(--lime);
    -webkit-text-stroke: 2px var(--navy);
    paint-order: stroke fill;
    text-shadow: 0 0 10px rgba(255,255,255,0.8);
    white-space: nowrap;
  }
  .tagline span { position: absolute; font-size: 52px; line-height: 1; letter-spacing: 1px; }
  .tagline .t1 { left: 360px; top: 540px; }
  .tagline .t2 { left: 425px; top: 608px; }

  .rule-soft {
    position: absolute;
    left: 66px; top: 966px;
    width: 955px; height: 14px;
    background: rgba(120,205,225,0.55);
  }
  .author-band {
    position: absolute;
    left: 66px; top: 993px;
    width: 955px; height: 56px;
    background: linear-gradient(90deg, #3aa9da, var(--blue) 60%, #4bb3dc);
    border-top: 2px solid rgba(255,255,255,0.5);
    border-bottom: 2px solid rgba(255,255,255,0.5);
  }
  .author-name {
    position: absolute;
    left: 347px; top: 1000px;
    color: var(--white);
    font-size: 38px;
    font-weight: 400;
    letter-spacing: 1px;
    white-space: nowrap;
    text-shadow: 0 1px 2px rgba(20,60,110,0.4);
  }
  .author-name .lead { font-size: 30px; margin-right: 8px; }

  .author-photo {
    position: absolute;
    left: 150px; top: 920px;
    width: 168px; height: 164px;
    border: 9px solid #40b9ac;
    background: linear-gradient(160deg, #7fae7a 0%, #b9c9a0 45%, #d8dcd0 70%, #9fb79a 100%);
    box-shadow: 0 2px 6px rgba(0,60,80,0.3);
  }
</style>
</head>
<body>
  <main class="cover">
    <div class="scene-doors" role="img" aria-label="Photo of open double doors leading into a bright clinic corridor"></div>

    <aside class="spine">
      <div class="spine-title">PLANTING <small>GARDENS</small> AFTER <small>WINTER</small></div>
    </aside>

    <h1 class="title">
      <span class="title-line line-planting">Planting</span>
      <span class="title-line line-gardens">Gardens<span class="minor">after</span></span>
      <span class="title-line line-winter">Winter</span>
    </h1>

    <p class="tagline">
      <span class="t1">PLUS GROW BRIGHT</span>
      <span class="t2">MORNINGS WITHIN</span>
    </p>

    <div class="rule-soft"></div>
    <div class="author-band"></div>
    <div class="author-photo" role="img" aria-label="Portrait photo of the author"></div>
    <p class="author-name"><span class="lead">AUTHOR</span>MAREN HOLLOWAY</p>
  </main>
</body>
</html>
```